Carpentry company Needs a business card design

We need a design for a Carpentry / building company, business card. Please think of designs out of the ordinary and try to make it eye catching. Our existing logo will need to be incorporated in the design. However feel free to change the colours of the logo to suit your design. I would like to see some designs with green /black and orange incorporated into it.These are not the only colours accepted and all designs that appeal will be accepted.

Please contact me should you have any questions
Thanks Martin

Target Market(s)

General Public seeking carpentry work

Industry/Entity Type

Business

Contact Information for Business Card

- Current company logo ( colours can be changed)
-Phone number ,
- info@brelvanbuild.com.au
- brelvanbuild.com.au
-the facebook symbol

Font styles to use
Other font styles liked:
• You choose

Requirements
Must have
• Services we provide
• - Renovations
• -Deckings & Pergolas
• -Kitchens
• - Bathrooms
• - Intricate details
Nice to have
• an awesome design
Should not have
• Tools on the business card

```html
<!DOCTYPE html>
<html lang="en">
<head>
<meta charset="utf-8">
<title>Brelvan Build – Business Card</title>
<link rel="stylesheet" href="https://fonts.googleapis.com/css2?family=Open+Sans:ital,wght@0,400;0,600;0,700;0,800;1,700&display=swap">
<style>
  :root {
    --page: #e9e6e1;
    --card-dark: #1b1b1b;
    --card-light: #ffffff;
    --ink: #1e1e1e;
    --ink-soft: #444444;
    --accent: #f07c14;
    --on-dark: #f2f2f2;
    --divider: #d6d6d6;
  }
  * { box-sizing: border-box; margin: 0; padding: 0; }
  html, body {
    width: 1200px; height: 843px; overflow: hidden;
    background: var(--page);
    font-family: "Open Sans", Arial, sans-serif;
  }
  .canvas { position: relative; width: 1200px; height: 843px; }

  .card {
    position: absolute; width: 620px; height: 354px;
    box-shadow: 0 10px 28px rgba(0,0,0,.28);
    overflow: hidden;
  }

  /* Shared brand block */
  .brand { display: flex; flex-direction: column; }
  .brand-row { display: flex; align-items: flex-start; gap: 12px; }
  .brand-mark { width: 16px; height: 16px; background: var(--accent); margin-top: 8px; flex: none; }
  .brand-name {
    display: flex; flex-direction: column;
    font-size: 34px; font-weight: 800; letter-spacing: 1px; line-height: 1.05;
    white-space: nowrap;
  }

  /* Back of card */
  .card--back { left: 440px; top: 56px; background: var(--card-dark); color: var(--on-dark); }
  .card--back .brand { position: absolute; left: 58px; top: 104px; }
  .card--back .brand-name { color: var(--on-dark); }
  .card--back .brand-web {
    margin-top: 12px; color: var(--accent);
    font-size: 15px; font-weight: 600; letter-spacing: 2px; white-space: nowrap;
  }
  .services { position: absolute; left: 360px; top: 100px; }
  .services-title { font-size: 19px; font-weight: 700; font-style: italic; margin-bottom: 6px; }
  .services-list { list-style: none; font-size: 17px; line-height: 27px; }
  .services-list li::before {
    content: ""; display: inline-block; width: 6px; height: 6px;
    background: var(--accent); border-radius: 50%;
    margin-right: 8px; vertical-align: middle; position: relative; top: -2px;
  }

  /* Front of card */
  .card--front { left: 160px; top: 444px; background: var(--card-light); color: var(--ink); }
  .card--front .brand { position: absolute; left: 56px; top: 130px; }
  .card--front .brand-name { color: var(--ink); }

  .divider {
    position: absolute; left: 300px; top: 110px; width: 1px; height: 150px;
    background: var(--divider);
  }
  .contact { position: absolute; left: 330px; top: 108px; }
  .contact-name { font-size: 24px; font-weight: 600; margin-bottom: 10px; }
  .contact-role { color: var(--accent); font-weight: 400; }
  .contact-list { list-style: none; font-size: 17px; line-height: 28px; color: var(--ink-soft); }
  .contact-list li { display: flex; align-items: center; gap: 10px; }
  .contact-icon { width: 15px; height: 15px; flex: none; fill: var(--ink); }
  .contact-square { width: 13px; height: 13px; background: var(--ink); flex: none; margin: 0 1px; }

  .edge-band { position: absolute; left: 0; bottom: 0; width: 230px; height: 16px; background: var(--card-dark); }
  .edge-tab { position: absolute; left: 0; bottom: 16px; width: 16px; height: 22px; background: var(--accent); }
</style>
</head>
<body>
<main class="canvas">

  <section class="card card--back" aria-label="Business card back">
    <div class="brand">
      <div class="brand-row">
        <span class="brand-mark"></span>
        <span class="brand-name"><span>BRELVAN</span><span>BUILD</span></span>
      </div>
      <div class="brand-web">www.brelvanbuild.com.au</div>
    </div>
    <div class="services">
      <h2 class="services-title">Services</h2>
      <ul class="services-list">
        <li>Renovations</li>
        <li>Deckings &amp; Pergolas</li>
        <li>Kitchens</li>
        <li>Bathrooms</li>
        <li>Intricate details</li>
      </ul>
    </div>
  </section>

  <section class="card card--front" aria-label="Business card front">
    <div class="brand">
      <div class="brand-row">
        <span class="brand-mark"></span>
        <span class="brand-name"><span>BRELVAN</span><span>BUILD</span></span>
      </div>
    </div>
    <div class="divider"></div>
    <div class="contact">
      <p class="contact-name">Martin - <span class="contact-role">Owner</span></p>
      <ul class="contact-list">
        <li>
          <svg class="contact-icon" viewBox="0 0 24 24" aria-hidden="true"><path d="M6.6 10.8a15.1 15.1 0 0 0 6.6 6.6l2.2-2.2c.3-.3.7-.4 1-.2 1.1.4 2.3.6 3.6.6.6 0 1 .4 1 1V20c0 .6-.4 1-1 1A17 17 0 0 1 3 4c0-.6.4-1 1-1h3.5c.6 0 1 .4 1 1 0 1.3.2 2.5.6 3.6.1.3 0 .7-.2 1z"/></svg>
          612 555 0184
        </li>
        <li><span class="contact-square"></span>brelvanbuild</li>
        <li>
          <svg class="contact-icon" viewBox="0 0 24 24" aria-hidden="true"><path d="M2 5h20v14H2z M3.5 6.5 12 13l8.5-6.5" fill="none" stroke="#1e1e1e" stroke-width="2"/></svg>
          info@brelvanbuild.com.au
        </li>
        <li>
          <svg class="contact-icon" viewBox="0 0 24 24" aria-hidden="true"><circle cx="12" cy="12" r="10"/><path d="M2 12h20M12 2c3 3 3 17 0 20M12 2c-3 3-3 17 0 20" fill="none" stroke="#fff" stroke-width="1.4"/></svg>
          www.brelvanbuild.com.au
        </li>
      </ul>
    </div>
    <div class="edge-tab"></div>
    <div class="edge-band"></div>
  </section>

</main>
</body>
</html>
```